Testosterone clinic billboard

Design billboard for Male Testosterone therapy simple to the point but eye catching.
Contact info for the billboard - Vantorelix.com
Phone - 919-457-2186

Target Market(s)

Males with disposable income

Industry/Entity Type

medical

Requirements
Must have
• Testosterone Therapy, Erectile Dysfunction, Male Enhancement
Nice to have
• Simple, easy to read

```html
<!DOCTYPE html>
<html lang="en">
<head>
<meta charset="utf-8">
<title>Vantorelix Billboard</title>
<link href="https://fonts.googleapis.com/css2?family=Roboto:wght@400;700;900&family=Roboto+Condensed:wght@700&display=swap" rel="stylesheet">
<style>
  :root {
    --purple: #662a80;
    --purple-soft: #9b6fb5;
    --teal: #186a62;
    --page: #e6e7ea;
    --board: #f4f5f7;
    --white: #ffffff;
  }
  * { margin: 0; padding: 0; box-sizing: border-box; }
  html, body { width: 993px; height: 1200px; overflow: hidden; }
  body {
    background: var(--page);
    font-family: "Roboto", Arial, sans-serif;
    position: relative;
  }
  .billboard {
    position: absolute;
    left: 0; top: 351px;
    width: 993px; height: 497px;
    background: linear-gradient(100deg, #eef0f3 0%, var(--white) 55%, #f1f2f5 100%);
    overflow: hidden;
  }
  .photo-area {
    position: absolute;
    left: 0; top: 0;
    width: 446px; height: 497px;
    background:
      radial-gradient(ellipse 170px 230px at 200px 250px, #e9c6b2 0%, #d9ad97 55%, rgba(217,173,151,0) 100%),
      radial-gradient(circle 190px at 270px 200px, var(--purple-soft) 0%, var(--purple) 90%, rgba(102,42,128,0) 100%),
      linear-gradient(90deg, #d7d9dd 0%, #eceef1 100%);
  }
  .side-band {
    position: absolute;
    right: 0; top: 0;
    width: 38px; height: 497px;
    background: linear-gradient(var(--purple) 0 351px, var(--teal) 351px 100%);
  }
  .brand-name {
    position: absolute;
    left: 478px; top: 40px;
    width: 446px;
    text-align: center;
    font-family: "Roboto Condensed", "Arial Narrow", sans-serif;
    font-weight: 700;
    font-size: 104px;
    line-height: 1;
    color: var(--purple);
    letter-spacing: -1px;
  }
  .services {
    position: absolute;
    left: 563px; top: 190px;
    list-style: none;
    font-size: 23px;
    line-height: 32px;
    color: var(--purple);
  }
  .services li { display: flex; align-items: center; gap: 10px; }
  .services .dot {
    width: 12px; height: 12px; border-radius: 50%;
    background: var(--teal);
    flex: none;
  }
  .services strong { font-weight: 700; }
  .services .teal { color: var(--teal); }
  .phone-pill {
    position: absolute;
    left: 444px; top: 316px;
    width: 476px; height: 83px;
    clip-path: polygon(5% 0, 100% 0, 100% 100%, 0 100%);
    border-radius: 0 42px 42px 0;
    background: linear-gradient(90deg, var(--purple) 0%, #5a4b73 60%, var(--teal) 100%);
    color: var(--white);
    font-weight: 700;
    font-size: 55px;
    letter-spacing: 1px;
    display: flex; align-items: center; justify-content: center;
    padding-left: 24px;
  }
  .website {
    position: absolute;
    left: 446px; top: 422px;
    width: 480px;
    text-align: center;
    font-size: 31px;
    font-weight: 400;
    color: var(--purple);
  }
  .website .domain { color: var(--teal); }
</style>
</head>
<body>
  <main class="billboard">
    <div class="photo-area" role="img" aria-label="Photo of a woman with smooth skin touching her face, over a purple circle with treatment imagery"></div>

    <h1 class="brand-name">Vantorelix</h1>

    <ul class="services">
      <li><span class="dot"></span><span><strong class="teal">Testosterone</strong> Therapy</span></li>
      <li><span class="dot"></span><span>Erectile <strong>Dysfunction</strong></span></li>
      <li><span class="dot"></span><span><strong class="teal">Male</strong> Enhancement</span></li>
    </ul>

    <div class="phone-pill">919-457-2186</div>

    <p class="website">www.<span class="domain">Vantorelix</span>.com</p>

    <div class="side-band"></div>
  </main>
</body>
</html>
```